Ausgefallene Verpackung für Neuartige Hunde Leine
Zielgruppe
ZIELGRUPPE: HUNDEHALTER
Aufgabenstellung
Das Projekt ist bis zum 15.01.2021 online. Bis dahin werden noch Design Vorschläge angenommen da es durch Feiertage zu Verzögerungen kam.
Die Vorgaben wäre eine interessante nicht stereotypische Verpackung bzw Halterung für eine Hundeleine zu entwickeln wobei die Vorzüge der Leine ausreichend und ansprechend illustriert und bestenfalls die Handhabung (auf der Rückseite) erklärt ist.
Bitte 'outside the box' denken. Es muss im Regal irgendwie auffallen das das Produkt anders ist als die anderen Leinen.
Ausserdem soll möglichst wenig Verpackunsmüll entstehen und kein Plastik verwendet werden.
Ein Bild im Sinne von Foto soll nicht direkt darauf, aber es soll anhand der Verpackung ersichtlich werden um was es sich handelt und welchen Nutzen die Leine hat.
Projektbeschreibung:
Es geht um eine Antizugleine welche in einen einfachen System dem Hund um den Brust gelegt wird und mit einem Karabiner dann am Halsband wie eine normale Leine befestigt wird. Sobald er anzieht gibt es einen leichten Druck und er hört auf zuziehen.
Gerne schicke ich Ihnen ein Foto der Leine ggf am Hund.
Das gute ist das man z. B. kein extra Haltegeschirr braucht welches man umständlich anziehen muss oder ein Halsband was sich am Hals zuzieht.
Gerade für ältere Menschen von Vorteil wenn der Hund nicht so (ruckartig) anzieht.
Ohne grosses Training wird die ungehemmt Vowärtsbewegung gehemmt.
UPDATE AUF DESIGNER ANMERKUNGEN:
Es geht zuerst um die Verpackung und deren Form. Danach auf den Inhalt
Schlagworte:
- vermindert das ziehen
- eine Größe für alle
- kein extra Haltegeschirr notwendig
- kein zuziehen der Kehle
- Ausbruchsicher
- hergestellt in Deutschland
1) Anleitungsbildchen zu kleine Dateigröße:
= Die Anleitungsbildchen sind nur zur Verdeutlichung/ Erklärung der Anwendung der Leine. Falls Sie diese Erklärungen verwenden möchten dienen dienen die zur Zeit als Pla..

```html
<!DOCTYPE html>
<html lang="de">
<head>
<meta charset="utf-8">
<title>Pfotenweg – Verpackung Antizugleine</title>
<link rel="stylesheet" href="https://fonts.googleapis.com/css2?family=Quicksand:wght@500;600&display=swap">
<style>
  :root {
    --kraft: #b89072;
    --ink: #1e1a17;
    --berry: #a8003b;
    --cutline: #d4006b;
    --illustration: #8f7a55;
    --illustration-ring: #2f3a22;
    --page: #ffffff;
  }
  * { box-sizing: border-box; margin: 0; padding: 0; }
  html, body { width: 779px; height: 1200px; overflow: hidden; background: var(--page); }
  body { position: relative; font-family: "Quicksand", sans-serif; color: var(--ink); font-weight: 500; }

  .hang-card { position: absolute; left: 246px; top: 32px; width: 290px; height: 492px; background: var(--kraft); }
  .main-panel { position: absolute; left: 101px; top: 523px; width: 580px; height: 631px; background: var(--kraft); }

  .hang-hole { position: absolute; left: 0; top: 0; }

  .step-illustration {
    position: absolute; width: 74px; height: 74px; border-radius: 50%;
    background: var(--illustration); border: 3px solid var(--illustration-ring);
    left: 110px;
  }
  .step-text { position: absolute; left: 0; width: 290px; text-align: center; font-size: 11px; line-height: 14px; }

  .site-url { position: absolute; left: 200px; top: 8px; width: 190px; text-align: center; font-size: 18px; font-weight: 600; letter-spacing: 0.2px; }

  .benefit-list { position: absolute; left: 24px; top: 41px; list-style: none; font-size: 11px; line-height: 14px; }
  .benefit-list li { position: relative; padding-left: 15px; margin-bottom: 3px; }
  .benefit-list li::before { content: "✔"; position: absolute; left: 0; top: 0; font-size: 12px; }

  .product-copy { position: absolute; left: 170px; top: 43px; width: 250px; text-align: center; font-size: 11px; line-height: 14.5px; }

  .recycle-mark { position: absolute; left: 431px; top: 60px; width: 46px; height: 46px; border-radius: 50%; border: 3px solid var(--ink); }
  .material-note { position: absolute; left: 478px; top: 84px; font-size: 10px; transform: rotate(-90deg); transform-origin: center; white-space: nowrap; }

  .cut-lines, .size-badge { position: absolute; left: 0; top: 0; }

  .brand-name {
    position: absolute; left: 190px; top: 518px; width: 200px; text-align: center;
    font-size: 30px; font-weight: 600; transform: rotate(180deg);
  }
  .tear-strip { position: absolute; left: 138px; top: 591px; width: 295px; height: 5px; border-radius: 3px; background: var(--cutline); }
</style>
</head>
<body>
  <section class="hang-card">
    <svg class="hang-hole" width="290" height="60" viewBox="0 0 290 60">
      <rect x="94" y="24" width="102" height="18" rx="9" fill="var(--page)"/>
      <circle cx="145" cy="28" r="10" fill="var(--page)"/>
    </svg>

    <div class="step-illustration" style="top:71px" role="img" aria-label="Anleitung Schritt 1: Hände legen die Leine durch den Ring"></div>
    <p class="step-text" style="top:160px">Lorem ipsum dolor sit amet,<br>consectetuer adipiscing elit, sed diam<br>nonummy nibh euismod tincidunt ut<br>laoreet dolore magna aliquam erat volut</p>

    <div class="step-illustration" style="top:222px" role="img" aria-label="Anleitung Schritt 2: Karabiner am Halsband befestigen"></div>
    <p class="step-text" style="top:301px">Lorem ipsum dolor sit amet, consectetuer<br>adipiscing elit, sed diam nonummy nibh<br>euismod tincidunt ut.</p>

    <div class="step-illustration" style="top:357px" role="img" aria-label="Anleitung Schritt 3: Leine liegt um die Brust des Hundes"></div>
    <p class="step-text" style="top:448px">Lorem ipsum dolor sit amet,<br>consectetuer adipiscing elit, sed diam<br>nonummy nibh euismod tincidunt.</p>
  </section>

  <section class="main-panel">
    <p class="site-url">www.pfotenweg.com</p>

    <ul class="benefit-list">
      <li>vermindert das ziven</li>
      <li>kein zuziehen der Kehle</li>
      <li>kein extra Haltegeschirr<br>notwendig</li>
      <li>ausbruchsicher</li>
      <li>hergestellt in<br>Deutschland</li>
    </ul>

    <p class="product-copy">Lorem ipsum dolor sit amet, consectetuer adipiscing elit, sed diam nonummy nibh euismod tincidunt ut laoreet dolore magna aliquam erat volutpat. Ut wisi enim ad minim veniam, quis nostrud exerci tation ullamcorper suscipit lobortis nisl ut aliquip ex ea</p>

    <div class="recycle-mark"></div>
    <p class="material-note">100% Naturkarton</p>

    <svg class="cut-lines" width="580" height="631" viewBox="0 0 580 631">
      <g stroke="var(--cutline)" stroke-width="1" stroke-dasharray="36 36" stroke-dashoffset="-4">
        <line x1="-4" y1="163" x2="580" y2="163"/>
        <line x1="-4" y1="320" x2="580" y2="320"/>
        <line x1="-4" y1="477" x2="580" y2="477"/>
      </g>
    </svg>

    <svg class="size-badge" width="580" height="631" viewBox="0 0 580 631">
      <defs>
        <path id="badge-arc" d="M243 440 A66 66 0 1 1 340 349"/>
      </defs>
      <circle cx="302" cy="412" r="51" fill="var(--berry)"/>
      <path d="M267 374 A56 56 0 1 1 257 445" fill="none" stroke="var(--ink)" stroke-width="2"/>
      <text x="290" y="425" text-anchor="middle" font-family="Quicksand, sans-serif" font-weight="500" font-size="34" fill="var(--ink)">ROT</text>
      <text font-family="Quicksand, sans-serif" font-weight="500" font-size="19" fill="var(--ink)">
        <textPath href="#badge-arc">eine Größe für alle</textPath>
      </text>
    </svg>

    <p class="brand-name">Pfotenweg</p>
    <div class="tear-strip"></div>
  </section>
</body>
</html>
```